Business Card Design Project

I am a Chiropractor that is looking for a new business card.  Our logo was slightly changed lately, therefore need a new, more professional look.
We are a modern, non-stuffy chiropractic office.  Want a contemporary look that will let people know this is not your typical doctors office.  Our logo is red, and contains the name of our business: realign.  The u in the logo is green, stressing the most important part of our business: "u"

Target Market(s)
moderate to upper income bracket, family friendly
www.realignspine-example.com
Gordon Pell
Family Chiropractor
314 Hollis Rd
Bastrop, TX 78999
512.555.0147 phone
512.555.0148 fax
Industry/Entity Type
Business
Requirements
Must have
- www.realignspine-example.com
Gordon Pell
Family Chiropractor
314 Hollis Rd
Bastrop, TX 78999
512.555.0147 phone
512.555.0148 fax

```html
<!DOCTYPE html>
<html lang="en">
<head>
<meta charset="utf-8">
<title>Realign Business Card</title>
<link rel="stylesheet" href="https://fonts.googleapis.com/css2?family=Didact+Gothic&family=Questrial&display=swap">
<style>
  :root {
    --card-red: #ee3642;
    --paper: #ffffff;
    --page: #ffffff;
  }
  * { margin: 0; padding: 0; box-sizing: border-box; }
  html, body {
    width: 1200px;
    height: 720px;
    overflow: hidden;
    background: var(--page);
  }
  .card {
    position: relative;
    width: 1200px;
    height: 720px;
    background: var(--paper);
    font-family: "Didact Gothic", "Questrial", sans-serif;
    color: var(--card-red);
  }
  .card-frame {
    position: absolute;
    left: 37px;
    top: 40px;
    width: 1112px;
    height: 642px;
    border: 4px solid var(--card-red);
  }
  .brand-name {
    position: absolute;
    left: 120px;
    top: 150px;
    width: 460px;
    text-align: center;
    font-size: 116px;
    font-weight: 400;
    line-height: 1;
    letter-spacing: 2px;
    color: var(--card-red);
  }
  .contact {
    position: absolute;
    left: 757px;
    top: 344px;
    width: 370px;
    text-align: center;
    white-space: nowrap;
    font-style: normal;
  }
  .contact-name {
    font-size: 50px;
    line-height: 58px;
  }
  .contact-title {
    font-size: 30px;
    line-height: 40px;
    font-style: italic;
    margin-left: -20px;
  }
  .contact-street {
    font-size: 35px;
    line-height: 40px;
    margin-top: 4px;
  }
  .contact-city {
    font-size: 37px;
    line-height: 42px;
  }
  .contact-line {
    font-size: 32px;
    line-height: 44px;
    display: flex;
    justify-content: center;
    align-items: baseline;
  }
  .contact-label {
    font-size: 19px;
    width: 74px;
    text-align: left;
  }
  .contact-web {
    font-size: 27px;
    line-height: 40px;
  }
</style>
</head>
<body>
  <main class="card">
    <div class="card-frame"></div>
    <h1 class="brand-name">realign</h1>
    <address class="contact">
      <p class="contact-name">Gordon Pell</p>
      <p class="contact-title">Family Chiropractor</p>
      <p class="contact-street">314 Hollis Rd</p>
      <p class="contact-city">Bastrop, TX 78999</p>
      <p class="contact-line"><span class="contact-label">Phone:</span>512.555.0147</p>
      <p class="contact-line"><span class="contact-label">Fax:</span>512.555.0148</p>
      <p class="contact-web">www.realignspine-example.com</p>
    </address>
  </main>
</body>
</html>
```